1日1袋を食べると(寒天)、
基礎代謝が増し、免疫が上がる新しい健康食品です。
1カ月分で約8000円です。

決して安い商品でないと思いますので、
見合ったデザインをお願いします。
現在最終製造中の為、詳細のサイズがまだわかりません。
12~15cmの立方体をイメージしてください。
赤系、茶系、無彩色系
良いデザイン、雰囲気の合いそうな方がいらっしゃれば締め切る可能性があります。
報酬額を合計32000円追加しています。
よろしくお願いします。
すでにご提案頂いた皆様、
現在作成中の皆様、ご検討中の皆様

このタイミングで追記となり申し訳ございません。
大きな変更ではありませんが、デザインをされている皆様からすると
ご納得いただけないかもしれません。
その点に関しては申し訳ございません。

今すでにご提案を頂いているもの、
これからご提案して頂くもの、
これからの追記内容が反映されていなくても、評価軸は変わりませんので、ご安心下さい。
プロジェクト決定後、データ差し替えが発生しますが、
現時点で追記前の状態で作られていたとしても、審査には問題ございませんので、
その点に関してはご安心下さい。

【追記内容】
ロゴデザインが一部変更になりました。
※こちらが最終です。ここからの変更はありません。

・アーチ形のエフェクトからストレートに
・雫の中のデザインが変わりました

【追記データ】

新しいロゴと分解したデータをお送りします。
※aiデータはございません。

以上、よろしくお願い致します。

高級感・ロゴにあった雰囲気、シルバーのデザイン等、印象がマッチしたのが大きな要因、且つ箱の展開図も同時に提案頂き、全体のイメージもつかみやすかったのも大きな要因でした。

この度は、弊社の新商品に関するパッケージデザインにご提案頂きありがとうございました。
今回一つを選ばせて頂きましたが、今後も本商品は様々な展開をする予定です。
また機会が合いましたら是非ご提案をお待ちしております。

現在別のデザインもコンペ中です。本商品のPOP版ですので、もしご興味ございましたらご応募頂けますと嬉しいです。
今後ともどうぞよろしくお願い致します。

```html
<!DOCTYPE html>
<html lang="ja">
<head>
<meta charset="utf-8">
<title>LU&amp;MA Package Faces</title>
<link rel="stylesheet" href="https://fonts.googleapis.com/css2?family=Jost:wght@400;500;600&display=swap">
<style>
  :root {
    --stage: #ebe7e1;
    --coral: #ee5b5e;
    --blush: #f4cdd2;
    --paper: #fbfaf9;
    --faint-blush: #f7e3e6;
    --face-size: 460px;
  }
  * { box-sizing: border-box; margin: 0; padding: 0; }
  html, body {
    width: 1200px;
    height: 788px;
    overflow: hidden;
    background: var(--stage);
    font-family: "Jost", "Helvetica Neue", Arial, sans-serif;
  }
  .stage {
    width: 1200px;
    height: 788px;
    display: flex;
    align-items: center;
    justify-content: center;
    gap: 60px;
  }
  .box-face {
    width: var(--face-size);
    height: var(--face-size);
    background: var(--paper);
    box-shadow: 0 18px 40px rgba(80, 60, 50, 0.12);
  }

  /* Pattern face */
  .pattern-face {
    display: grid;
    grid-template-columns: repeat(3, 1fr);
    grid-template-rows: repeat(3, 1fr);
  }
  .tile {
    display: flex;
    flex-direction: column;
    align-items: center;
    justify-content: center;
    gap: 10px;
    color: var(--coral);
    font-weight: 500;
    letter-spacing: 0.12em;
  }
  .tile--coral { background: var(--coral); color: var(--paper); }
  .tile--blush { background: var(--blush); }
  .tile--paper { background: var(--paper); }
  .tile--wide { grid-column: span 2; }
  .tile .wordmark { font-size: 44px; }
  .tile .wordmark--small { font-size: 22px; }
  .tile .wordmark--faint { font-size: 30px; color: var(--paper); }
  .dot {
    width: 64px;
    height: 64px;
    border-radius: 50%;
    background: currentColor;
  }
  .tile--coral .dot { background: var(--paper); }
  .dot--small { width: 36px; height: 36px; }

  /* Plain front face */
  .front-face {
    position: relative;
    display: flex;
    flex-direction: column;
    align-items: center;
    padding-top: 132px;
    color: var(--coral);
  }
  .front-face .wordmark {
    font-size: 50px;
    font-weight: 500;
    letter-spacing: 0.14em;
  }
  .front-face .mark {
    width: 52px;
    height: 52px;
    border-radius: 50%;
    background: var(--coral);
    margin: 16px 0 18px;
  }
  .front-face .tagline {
    font-size: 19px;
    font-weight: 400;
    letter-spacing: 0.04em;
  }
  .texture-area {
    position: absolute;
    right: 58px;
    top: 236px;
    width: 112px;
    height: 140px;
    background: linear-gradient(160deg, var(--faint-blush), rgba(247, 227, 230, 0.35));
    z-index: 0;
  }
  .front-face > * { position: relative; z-index: 1; }
  .front-face > .texture-area { position: absolute; z-index: 0; }
</style>
</head>
<body>
  <main class="stage">
    <section class="box-face pattern-face" aria-label="Patterned side of the box">
      <div class="tile tile--coral"><span class="dot"></span></div>
      <div class="tile tile--paper tile--wide"><span class="wordmark">LU&amp;MA</span></div>

      <div class="tile tile--blush tile--wide"><span class="wordmark">LU&amp;MA</span></div>
      <div class="tile tile--coral"><span class="dot dot--small"></span><span class="wordmark wordmark--small">LU&amp;MA</span></div>

      <div class="tile tile--paper"><span class="dot dot--small"></span><span class="wordmark wordmark--small">LU&amp;MA</span></div>
      <div class="tile tile--coral"><span class="dot"></span></div>
      <div class="tile tile--blush"><span class="wordmark wordmark--faint">LU&amp;MA</span></div>
    </section>

    <section class="box-face front-face" aria-label="Front of the box">
      <div class="texture-area" role="img" aria-label="Faint honeycomb texture in pale pink"></div>
      <h1 class="wordmark">LU&amp;MA</h1>
      <span class="mark"></span>
      <p class="tagline">LUSTER &amp; Mild Armor</p>
    </section>
  </main>
</body>
</html>
```